Brontaro Web Site

Redesigned web site for Brontaro Ltd (www.brontaro-example.co.uk). This is to feature new logo (attached). Brontaro Ltd is a company which specialises in Geographic Information Systems and Geographic data - we call ourselves GIS Data Specialists. We are looking for something which conveys our professionalism and our experience. There will be more pages than on the current Brontaro website. There will be: Home, Data Migration, Data Cleansing & Validation, Data Analysis, Data Maintenance, Data Quality and an About Us page. All these should be accessible from each page on the website.
Updates
I didn't really think to say that the content of the web site is going to change from the current one we have. There will be more pages than on the current one. They will be: Home, Data Migration, Data Cleansing & Validation, Data Analysis, Data Maintenance, Data Quality and an About Us page. All these should be accessible from each page on the website. I didn't really think through the fact that the number of pages / areas to access can influence the layout of the site, sorry.
Target Market(s)
Utility Companies (e.g. telecommunications providers, energy companies), local government.
Industry/Entity Type
It Company
Look and feel

```html
<!DOCTYPE html>
<html lang="en">
<head>
<meta charset="utf-8">
<title>Brontaro – GIS Data Specialists</title>
<link href="https://fonts.googleapis.com/css2?family=Arimo:wght@400;700&family=Ubuntu:wght@400;500&display=swap" rel="stylesheet">
<style>
  :root {
    --page-bg: #403d3e;
    --frame: #7a797a;
    --frame-dark: #5d5c5d;
    --nav-green: #b3d24a;
    --nav-text: #1c1c1c;
    --nav-rule: #8ea43a;
    --white: #ffffff;
    --card-head: #7a7778;
    --card-text: #8a8889;
    --card-border: #9c9a9b;
    --footer-text: #8c8a8b;
    --orange: #e38e0c;
    --orange-dark: #b56a05;
    --teal: #1aa6bd;
    --teal-dark: #0f7f92;
    --green: #7ccd1c;
    --green-dark: #55a00e;
  }
  * { box-sizing: border-box; margin: 0; padding: 0; }
  html, body { width: 1200px; height: 1030px; overflow: hidden; }
  body { background: var(--page-bg); font-family: "Arimo", Arial, sans-serif; color: var(--white); position: relative; }

  .brand { position: absolute; left: 150px; top: 62px; display: flex; align-items: center; gap: 14px; }
  .brand-dot { width: 44px; height: 44px; border-radius: 50%; background: var(--white); }
  .brand-name { font-family: "Ubuntu", sans-serif; font-weight: 500; font-size: 40px; line-height: 1; color: var(--white); }
  .brand-tag { position: absolute; left: 210px; top: 102px; font-size: 16px; color: #d8d8d8; }

  .contact { position: absolute; right: 135px; top: 31px; font-size: 14px; line-height: 20px; text-align: right; }
  .contact li { list-style: none; display: flex; justify-content: flex-end; align-items: center; gap: 8px; }
  .contact svg { width: 16px; height: 14px; }

  .nav-frame { position: absolute; left: 120px; top: 148px; width: 300px; height: 298px; }
  .nav { position: absolute; left: 156px; top: 178px; width: 236px; }
  .nav li { list-style: none; border-bottom: 1px solid var(--nav-rule); margin-left: 14px; height: 32px; position: relative; }
  .nav a { position: absolute; left: 1px; top: 6px; font-size: 17px; color: var(--nav-text); text-decoration: none; -webkit-text-stroke: 0.25px var(--nav-text); }
  .nav li::before { content: ""; position: absolute; left: -13px; top: 10px; border-left: 5px solid #111; border-top: 4px solid transparent; border-bottom: 4px solid transparent; }

  .hero-frame { position: absolute; left: 413px; top: 95px; width: 672px; height: 352px; }
  .hero-photo { position: absolute; left: 424px; top: 106px; width: 650px; height: 330px; border-radius: 10px;
    background: radial-gradient(ellipse at 45% 45%, #bdbdbd 0%, #8f8f8f 45%, #5f5f5f 100%); }
  .hero-note { position: absolute; left: 893px; top: 128px; width: 160px; font-size: 12.5px; line-height: 15px; text-align: center; color: var(--white); }
  .ribbon { position: absolute; left: 829px; width: 262px; height: 48px; }
  .ribbon span { position: absolute; left: 26px; top: 10px; font-family: "Ubuntu", sans-serif; font-weight: 500; font-size: 17px; color: var(--white); letter-spacing: .2px; }

  .content { position: absolute; left: 150px; top: 470px; width: 900px; height: 448px;
    background: linear-gradient(to bottom, #4d4a4b, #454243 80%, #423f40); box-shadow: 0 0 30px rgba(0,0,0,.15); }
  .content h1 { position: absolute; left: 36px; top: 28px; font-weight: 400; font-size: 26px; }
  .content .intro { position: absolute; left: 38px; top: 70px; width: 830px; font-size: 16px; line-height: 26px; }

  .card { position: absolute; top: 159px; width: 270px; height: 247px; border: 3px solid var(--card-border); border-radius: 18px;
    background: linear-gradient(to bottom, #c3c3c3, #e6e6e6 60%, #ffffff); }
  .card h2 { position: absolute; left: 17px; top: 18px; font-size: 26px; font-weight: 700; color: var(--card-head); }
  .card p { position: absolute; left: 17px; top: 56px; width: 240px; font-size: 16px; line-height: 26px; color: var(--card-text); }
  .card .more { position: absolute; right: 14px; bottom: 8px; font-size: 12px; color: #2a2a2a; text-decoration: none; }

  .footer-brand { position: absolute; left: 146px; top: 940px; display: flex; align-items: center; gap: 6px; }
  .footer-brand .brand-dot { width: 22px; height: 22px; background: #9a9899; }
  .footer-brand .brand-name { font-size: 20px; color: #bdbbbc; }
  .footer-tag { position: absolute; left: 176px; top: 964px; font-size: 8px; color: #8f8d8e; }
  .legal { position: absolute; right: 155px; top: 948px; font-size: 13px; color: var(--footer-text); text-align: center; }
  .legal nav { font-size: 11px; margin-top: 4px; color: #a9a7a8; }
  .legal a { color: #a9a7a8; text-decoration: none; }
</style>
</head>
<body>

<header>
  <div class="brand"><span class="brand-dot"></span><span class="brand-name">Brontaro</span></div>
  <div class="brand-tag">GIS Data Specialists</div>

  <ul class="contact">
    <li><svg viewBox="0 0 16 14"><path d="M3 1c1 0 2 2 2 3s-1 1-1 2 2 3 3 3 1-1 2-1 3 1 3 2-1 2-2 2C6 12 2 8 2 3c0-1 0-2 1-2z" fill="none" stroke="#ddd" stroke-width="1.2"/></svg>+44 (0) 1632 960 360</li>
    <li><svg viewBox="0 0 16 14"><rect x="1" y="5" width="14" height="8" fill="none" stroke="#ddd"/><rect x="4" y="1" width="8" height="4" fill="none" stroke="#ddd"/><path d="M4 8h8M4 10h8" stroke="#ddd"/></svg>+44 (0) 1632 960 303</li>
    <li><svg viewBox="0 0 16 14"><rect x="1" y="3" width="13" height="9" fill="none" stroke="#ddd"/><path d="M1 3l6.5 5L14 3" fill="none" stroke="#ddd"/></svg>contact@brontaro-example.co.uk</li>
  </ul>

  <svg class="nav-frame" viewBox="0 0 300 298">
    <path d="M18 0H290l10 10V288l-10 10H18L0 280V18z" fill="var(--frame-dark)"/>
    <path d="M22 8H110l10 6H230l8-6H293V290H22L8 276V22z" fill="var(--nav-green)"/>
  </svg>
  <nav>
    <ul class="nav">
      <li><a href="#">Home</a></li>
      <li><a href="#">Data Migration</a></li>
      <li><a href="#">Data Cleansing &amp; Validation</a></li>
      <li><a href="#">Data Analysis</a></li>
      <li><a href="#">Data Maintenance</a></li>
      <li><a href="#">Data Quality</a></li>
      <li><a href="#">About Us</a></li>
    </ul>
  </nav>

  <svg class="hero-frame" viewBox="0 0 672 352">
    <path d="M18 0H655l17 17V335l-17 17H18L0 334V18z" fill="var(--frame)"/>
  </svg>
  <div class="hero-photo" role="img" aria-label="Photograph of a businesswoman in a dark suit touching a glowing point on a translucent world map"></div>
  <p class="hero-note">We can be on hand to help with any or all parts of your data projects via: &#9662;</p>

  <svg class="ribbon" style="top:183px" viewBox="0 0 262 48"><path d="M20 0H252l8 6v36l-8 6H20L0 21z" fill="var(--orange)"/><path d="M252 0l8 6v36l-8 6z" fill="var(--orange-dark)"/></svg>
  <div class="ribbon" style="top:183px"><span>DATA CONSULTANCY</span></div>
  <svg class="ribbon" style="top:238px" viewBox="0 0 262 48"><path d="M20 0H252l8 6v36l-8 6H20L0 21z" fill="var(--teal)"/><path d="M252 0l8 6v36l-8 6z" fill="var(--teal-dark)"/></svg>
  <div class="ribbon" style="top:238px"><span>SOFTWARE DEVELOPMENT</span></div>
  <svg class="ribbon" style="top:292px" viewBox="0 0 262 48"><path d="M20 0H252l8 6v36l-8 6H20L0 21z" fill="var(--green)"/><path d="M252 0l8 6v36l-8 6z" fill="var(--green-dark)"/></svg>
  <div class="ribbon" style="top:292px"><span>SYSTEM CONSULTANCY</span></div>
</header>

<main class="content">
  <h1>Welcome to Brontaro</h1>
  <p class="intro">Brontaro was founded in 1994 by a group of geospatial software engineers that recognised the significant value that data, and the systems used to store and analyse this data, could bring to business.</p>

  <section class="card" style="left:36px">
    <h2>Our Customers:</h2>
    <p style="width:232px">We have worked with over 200 companies in a myriad of market sectors - from utilities, local and central government, oil and gas, to many spheres of the marine industry.</p>
    <a class="more" href="#">read more...</a>
  </section>
  <section class="card" style="left:315px">
    <h2 style="left:14px">Our Pedigree:</h2>
    <p style="left:14px">We provide a vast bank of knowl-edge and experience to offer an all encompassing service. This ensures that you, as a customer, reap the maximum benefits from your data and systems ...</p>
    <a class="more" href="#">read more...</a>
  </section>
  <section class="card" style="left:594px">
    <h2 style="left:14px">Our People:</h2>
    <p style="left:16px">We have a wide ranging skill set including PROVANT 2 qualified Project Managers, fully qualified Software Developers and Experienced Data Consultants.</p>
    <a class="more" href="#">read more...</a>
  </section>
</main>

<footer>
  <div class="footer-brand"><span class="brand-dot"></span><span class="brand-name">Brontaro</span></div>
  <div class="footer-tag">GIS Data Specialists</div>
  <div class="legal">
    © 2010 Brontaro Ltd. Registered in Scotland No. 100234
    <nav><a href="#">Terms and Conditions</a> &nbsp; | &nbsp; <a href="#">Privacy Policy</a></nav>
  </div>
</footer>

</body>
</html>
```